christmas poster

Gift Vouchers Promotion

Buy 3 of Any Value
Get 1 More Free

The Poster Should be very modern but with a relevance to Christmas

Target Market(s)

Affluent Clients

Font styles to use
Decorative

Colors
ec1f27

Requirements
Must have
• Modern Clean Feel but Relevant to Christmas
Nice to have
• The Offer:
• Buy 3 Gift Vouchers and Receive 1 More Fee
• MUST be Big and Bold
• Include Logo

```html
<!DOCTYPE html>
<html lang="en">
<head>
<meta charset="utf-8">
<title>Buy 3 Gift Vouchers and Receive 1 Free</title>
<link rel="stylesheet" href="https://fonts.googleapis.com/css2?family=Arimo&family=Tinos:wght@700&family=Yellowtail&display=swap">
<style>
  :root {
    --festive-red: #bf1e2e;
    --ribbon-red: #b0121f;
    --bow-light: #e3323c;
    --bow-dark: #9a0f1a;
    --white: #ffffff;
    --ink: #111111;
    --divider-grey: #a7a9ac;
    --footer-text: #333333;
  }
  * { margin: 0; padding: 0; box-sizing: border-box; }
  html, body { width: 828px; height: 1200px; overflow: hidden; background: var(--white); }
  .poster {
    position: relative;
    width: 828px;
    height: 1200px;
    overflow: hidden;
    background: var(--white);
  }
  .offer-panel {
    position: absolute;
    left: 0; top: 0;
    width: 828px; height: 993px;
    background: var(--festive-red);
  }
  .divider-band {
    position: absolute;
    left: 0; top: 993px;
    width: 828px; height: 27px;
    background: var(--divider-grey);
  }
  .headline { position: absolute; left: 0; top: 0; }
  .serif { font-family: 'Tinos', 'Times New Roman', serif; font-weight: 700; }
  .script { font-family: 'Yellowtail', cursive; }
  .voucher-card {
    position: absolute;
    left: 107px; top: 673px;
    width: 637px; height: 254px;
    background: var(--white);
    box-shadow: 0 6px 14px rgba(0,0,0,0.28);
  }
  .card-text { position: absolute; left: 0; top: 0; }
  .bow-art {
    position: absolute;
    left: 100px; top: 653px;
    width: 250px; height: 200px;
    background: radial-gradient(ellipse at 50% 45%, var(--bow-light) 0%, var(--ribbon-red) 60%, var(--bow-dark) 100%);
  }
  .ribbon-art {
    position: absolute;
    left: 548px; top: 730px;
    width: 200px; height: 230px;
    background: linear-gradient(135deg, var(--bow-light) 0%, var(--ribbon-red) 55%, var(--bow-dark) 100%);
  }
  .brand {
    position: absolute;
    left: 0; top: 1060px;
    width: 828px;
    text-align: center;
  }
  .brand-name {
    font-family: 'Tinos', 'Times New Roman', serif;
    font-weight: 700;
    font-size: 46px;
    color: var(--festive-red);
    letter-spacing: 1px;
  }
  .contact-line {
    position: absolute;
    left: 0; top: 1168px;
    width: 828px;
    text-align: center;
    font-family: 'Arimo', Arial, sans-serif;
    font-size: 14.5px;
    color: var(--footer-text);
  }
  .contact-line .sep { color: var(--festive-red); margin: 0 6px; }
</style>
</head>
<body>
<main class="poster">
  <section class="offer-panel"></section>

  <svg class="headline" width="828" height="660" viewBox="0 0 828 660" aria-label="Buy 3 gift vouchers and receive 1 free">
    <text class="serif" x="460" y="123" font-size="72" fill="var(--white)" textLength="233" lengthAdjust="spacingAndGlyphs">BUY 3</text>
    <text class="script" x="205" y="255" font-size="175" fill="var(--white)" textLength="395" lengthAdjust="spacingAndGlyphs">Gift</text>
    <text class="serif" x="96" y="393" font-size="122" fill="var(--white)" textLength="635" lengthAdjust="spacingAndGlyphs">VOUCHERS</text>
    <line x1="29" y1="441" x2="127" y2="441" stroke="var(--white)" stroke-width="2"/>
    <text class="serif" x="138" y="451" font-size="27" fill="var(--white)" textLength="515" lengthAdjust="spacing">AND RECEIVE</text>
    <line x1="664" y1="441" x2="800" y2="441" stroke="var(--white)" stroke-width="2"/>
    <text class="serif" x="91" y="620" font-size="190" fill="var(--white)" textLength="640" lengthAdjust="spacingAndGlyphs">1 FREE</text>
  </svg>

  <div class="voucher-card"></div>

  <svg class="card-text" width="828" height="960" viewBox="0 0 828 960" aria-label="Gift vouchers card">
    <text class="script" x="353" y="818" font-size="110" fill="var(--ink)" textLength="180" lengthAdjust="spacingAndGlyphs">Gift</text>
    <text class="serif" x="229" y="890" font-size="48" fill="var(--ink)" textLength="307" lengthAdjust="spacingAndGlyphs">VOUCHERS</text>
  </svg>

  <div class="bow-art" role="img" aria-label="Red satin gift bow with golden sparkles"></div>
  <div class="ribbon-art" role="img" aria-label="Red satin ribbon wrapping the card corner with sparkles"></div>

  <div class="divider-band"></div>

  <footer>
    <div class="brand"><span class="brand-name">Velvetleaf Salon &amp; Spa</span></div>
    <p class="contact-line">
      418-420 Harbour View Road<span class="sep">•</span>Kingsgrove Park, NSW 2208<span class="sep">•</span>(02) 9000 1234<span class="sep">•</span>www.velvetleaf.net.au
    </p>
  </footer>
</main>
</body>
</html>
```